Nobody Left the Lantern Burning - Tom Halvery - CD Cover Design Project

Single Cover for CD & Online media e.g. Tunebox Graphics
The first song release from Tom Halvery will be the track 'Nobody Left the Lantern Burning'.
For the release the single requires artwork that is eye catching, seriously professional & meets the requirements of Disc Sprout, Tunebox and also a physical copy on CD.
Track listings for CD will be:
1. Nobody Left the Lantern Burning
2. Nobody Left the Lantern Burning - Instrumental
see details in this link:
http://members.discsprout-example.com/faq.aspx
http://selfmadesound.discsprout-example.com/2009/11/avoid-album-art-atrocities/
http://answers.quorvex-example.com/question/index?qid=20111015141433AAdDTmH
Any advice on this would be greatly appreciated,
I would also like the two logo's I have uploaded to be used,
one is the Tom Halvery logo and the other is for Milbrook & Tandy Records logo (please remove the R and replace with a C for copyright.)
There are four high res photo shopped pictures of Tom Halvery and another zip file of many others, it would be nice to include one of these maybe on the 2nd page or back of the CD. Please don't use them as the front cover.
I imagine an Art Deco illustration but please listen to the track and let it inspire you.
Good Luck
Updates
I don't feel this is what I'm looking for, the design needs to refelct a broken heart without being a picture of a broken heart
Reason: No design has been what we are after so far so the deadline has been extended and the budget increased.

```html
<!DOCTYPE html>
<html lang="en">
<head>
<meta charset="utf-8">
<title>Tom Halvery – Nobody Left the Lantern Burning – CD Cover Set</title>
<link rel="stylesheet" href="https://fonts.googleapis.com/css2?family=Open+Sans:wght@400&family=Oleo+Script&family=Playfair+Display:wght@700&family=Marcellus&display=swap">
<style>
  :root {
    --board: #2e3031;
    --label: #ffffff;
    --ink-black: #000000;
    --name-cream: #ddd6c8;
    --track-white: #f2efe8;
    --label-ink: #5b1a2a;
    --front-dark: #0d1a22;
    --front-blue: #1f5a80;
    --front-tan: #8f6a3c;
    --front-warm: #b0742a;
    --inside-dark: #120606;
    --inside-maroon: #4a0a06;
    --inside-olive: #4a4a26;
    --inside-teal: #0c2c36;
    --back-navy: #081430;
    --back-olive: #3a3a20;
    --back-rust: #5a2410;
    --back-leaf: #244f16;
  }
  * { margin: 0; padding: 0; box-sizing: border-box; }
  html, body { width: 1200px; height: 1000px; overflow: hidden; background: var(--board); }
  .board { position: relative; width: 1200px; height: 1000px; background: var(--board); }

  .panel-label {
    position: absolute;
    font-family: "Open Sans", sans-serif;
    font-weight: 400;
    font-size: 44px;
    color: var(--label);
    letter-spacing: 0.5px;
    transform: translateX(-50%);
    white-space: nowrap;
  }
  .panel-label--front { left: 333px; top: 28px; }
  .panel-label--inside { left: 886px; top: 28px; }
  .panel-label--back { left: 600px; top: 532px; }

  .cover { position: absolute; background: var(--ink-black); overflow: hidden; }
  .cover-art { position: absolute; inset: 0; }
  .cover--front { left: 121px; top: 93px; width: 426px; height: 426px; }
  .cover--inside { left: 685px; top: 93px; width: 428px; height: 428px; }
  .cover--back { left: 404px; top: 593px; width: 394px; height: 394px; }

  .cover--front .cover-art {
    background:
      radial-gradient(circle at 75% 55%, var(--front-warm) 0%, transparent 45%),
      linear-gradient(135deg, var(--front-dark) 0%, var(--front-blue) 35%, var(--front-tan) 70%, var(--front-dark) 100%);
  }
  .cover--inside .cover-art {
    background:
      radial-gradient(circle at 75% 25%, var(--inside-maroon) 0%, transparent 55%),
      radial-gradient(circle at 75% 85%, var(--inside-teal) 0%, transparent 55%),
      linear-gradient(160deg, var(--inside-dark) 0%, var(--inside-olive) 45%, var(--inside-dark) 100%);
  }
  .cover--back .cover-art {
    background:
      radial-gradient(circle at 20% 15%, var(--back-navy) 0%, transparent 50%),
      radial-gradient(circle at 80% 55%, var(--back-rust) 0%, transparent 55%),
      radial-gradient(circle at 25% 85%, var(--back-leaf) 0%, transparent 55%),
      var(--back-olive);
  }

  .artist-name {
    position: absolute;
    font-family: "Oleo Script", cursive;
    color: var(--name-cream);
    line-height: 1;
    white-space: nowrap;
  }
  .cover--front .artist-name { left: 16px; top: 150px; font-size: 44px; }
  .cover--front .artist-name .line-2 { display: block; margin-left: -4px; margin-top: 16px; font-size: 58px; }
  .cover--back .artist-name { left: 64px; top: 128px; font-size: 52px; }
  .cover--back .artist-name .line-2 { display: block; margin-left: -4px; margin-top: 14px; font-size: 76px; }

  .label-block {
    position: absolute;
    left: 319px; top: 358px; width: 107px; height: 46px;
    background: #ffffff;
    display: flex; flex-direction: column; justify-content: center;
    padding: 0 6px;
    gap: 3px;
  }
  .label-block span {
    font-family: "Open Sans", sans-serif;
    font-size: 7.5px;
    color: var(--label-ink);
    line-height: 1.1;
    white-space: nowrap;
  }

  .track-list {
    position: absolute;
    left: 0; right: 0; top: 145px;
    text-align: center;
  }
  .track-list h2 {
    font-family: "Playfair Display", serif;
    font-weight: 700;
    font-size: 21px;
    color: var(--track-white);
    letter-spacing: 0.3px;
    margin-bottom: 44px;
    padding-left: 16px;
  }
  .track-list ol { list-style: none; }
  .track-list li {
    font-family: "Marcellus", serif;
    font-size: 14.5px;
    color: var(--track-white);
    margin-bottom: 13px;
    white-space: nowrap;
  }
  .track-list li.track-1 { padding-left: 18px; }
</style>
</head>
<body>
<main class="board">

  <h1 class="panel-label panel-label--front">FRONT COVER</h1>
  <section class="cover cover--front">
    <div class="cover-art" role="img" aria-label="Photograph of Tom Halvery in blue and orange light, overlaid with translucent coloured geometric shapes"></div>
    <div class="artist-name">Tom<span class="line-2">Halvery</span></div>
    <div class="label-block">
      <span>Tom Halvery</span>
      <span>Milbrook &amp; Tandy Records</span>
    </div>
  </section>

  <h1 class="panel-label panel-label--inside">INTERNAL COVER</h1>
  <section class="cover cover--inside">
    <div class="cover-art" role="img" aria-label="Abstract artwork of overlapping translucent shapes in maroon, olive and teal on black"></div>
    <div class="track-list">
      <h2>TRACK LIST</h2>
      <ol>
        <li class="track-1">1. Nobody Left the Lantern Burning</li>
        <li class="track-2">2. Nobody Left the Lantern Burning - Instrumental</li>
      </ol>
    </div>
  </section>

  <h1 class="panel-label panel-label--back">BEHIND COVER</h1>
  <section class="cover cover--back">
    <div class="cover-art" role="img" aria-label="Abstract artwork of overlapping translucent shapes in navy, green, olive and rust on black"></div>
    <div class="artist-name">Tom<span class="line-2">Halvery</span></div>
  </section>

</main>
</body>
</html>
```